Redesign of an insurance website

Attached is an insurance website that I need to redesign. Currently the website is too dark. I like for example www.brenvalo.com . Could you make the website lighter and change the structure a little so that it is more user friendly?

Industry/Entity Type

Insurance

Number of Pages Required

4 page

```html
<!DOCTYPE html>
<html lang="cs">
<head>
<meta charset="utf-8">
<title>Pojistivo.cz – Najdete nejvyhodnejsi pojisteni</title>
<link href="https://fonts.googleapis.com/css2?family=Open+Sans:wght@300;400;600;700&display=swap" rel="stylesheet">
<style>
:root{
  --orange:#f07f1e;
  --blue:#1b4f9c;
  --ink:#1e1e1e;
  --text:#3c3c3c;
  --muted:#8c8c8c;
  --hero-bg:#e9eaed;
  --why-bg:#f5f5f5;
  --info-bg:#ececec;
  --band-bg:#d3d3d3;
  --white:#ffffff;
  --placeholder-top:#dcdde0;
  --placeholder-bottom:#cfd0d4;
}
*{box-sizing:border-box;margin:0;padding:0}
html,body{width:1017px;height:1200px;overflow:hidden;background:var(--white)}
body{font-family:"Open Sans",sans-serif;color:var(--text);position:relative}
.abs{position:absolute}
a{color:inherit;text-decoration:none}

/* header */
.site-header{position:absolute;left:0;top:0;width:1017px;height:64px;background:var(--white)}
.main-nav{left:39px;top:23px;font-size:11px;color:var(--ink);display:flex;gap:18px}
.brand{left:0;width:1017px;top:19px;text-align:center;font-size:19px;font-weight:700;color:var(--blue);letter-spacing:.3px}
.btn-register{left:788px;top:21px;width:88px;height:22px;border:1px solid #555;font-size:8px;font-weight:700;color:var(--ink);display:flex;align-items:center;justify-content:center}
.login{left:901px;top:24px;font-size:11px;color:var(--ink)}

/* hero */
.hero{left:0;top:64px;width:1017px;height:424px;background:var(--hero-bg)}
.hero-title{font-size:15px;font-weight:600;color:var(--ink)}
.category-list .cat{position:absolute;left:124px;width:200px;height:50px;display:flex;align-items:center}
.cat-icon{width:50px;height:50px;border-radius:50%;border:1.5px solid #444;display:flex;align-items:center;justify-content:center;background:transparent}
.cat.active .cat-icon{background:var(--orange);border-color:var(--orange)}
.cat-label{margin-left:33px;font-size:10.5px;font-weight:600;color:var(--ink);line-height:14px}
.house-visual{left:290px;top:190px;width:334px;height:200px;border-radius:6px;background:linear-gradient(180deg,var(--placeholder-top) 0%,var(--placeholder-bottom) 100%)}
.quote-form .field{position:absolute;left:649px;width:244px;height:40px;background:var(--white);border:1px solid #c7c7c7;font-size:12px;color:#9a9a9a;padding:0 15px;display:flex;align-items:center}
.consent{left:649px;top:334px;font-size:11px;color:#666;display:flex;align-items:center;gap:13px}
.consent .box{width:14px;height:14px;border:1px solid #ccc;background:var(--white);display:flex;align-items:center;justify-content:center}
.consent .box i{width:6px;height:6px;background:var(--orange)}
.consent u{text-decoration:underline}
.btn-price{left:648px;top:373px;width:163px;height:37px;background:var(--orange);color:var(--white);font-size:15px;font-weight:700;letter-spacing:.5px;display:flex;align-items:center;justify-content:center}

/* why */
.why{left:0;top:488px;width:1017px;height:256px;background:var(--why-bg)}
.why-title{left:0;width:1046px;top:537px;text-align:center;font-size:15px;font-weight:600;color:var(--ink)}
.benefit{position:absolute;font-size:13px;font-weight:300;color:var(--text);display:flex;align-items:center;gap:19px;white-space:nowrap}
.benefit.secondary{color:var(--muted)}

/* info */
.info{left:0;top:744px;width:1017px;height:256px;background:var(--info-bg)}
.review-visual{left:124px;top:776px;width:221px;height:192px;border-radius:9px;background:radial-gradient(circle at 40% 60%,#fafafa 0%,#e2e2e2 60%,#b9b9b9 100%)}
.info-col{width:252px}
.info-col h3{font-size:12.5px;font-weight:600;color:var(--ink);line-height:15px;margin-bottom:15px;min-height:30px}
.info-col p{font-size:10.3px;font-weight:300;line-height:15.5px;color:#333}

/* newsletter band */
.newsletter{left:0;top:1000px;width:1017px;height:73px;background:var(--band-bg)}
.band-brand{left:125px;top:1025px;font-size:18px;font-weight:700;color:var(--white)}
.band-label{left:390px;top:1027px;font-size:12px;font-weight:600;color:var(--white)}
.band-input{left:559px;top:1022px;width:217px;height:29px;background:#dcdcdc;font-size:9px;color:var(--white);padding:0 12px;display:flex;align-items:center}
.band-btn{left:780px;top:1022px;width:113px;height:29px;background:var(--white);color:var(--orange);font-size:10px;font-weight:600;letter-spacing:.5px;display:flex;align-items:center;justify-content:center}

/* footer */
.legal{left:124px;top:1118px;font-size:10.5px;color:#777}
.copyright{left:124px;top:1139px;font-size:10.5px;color:#777}
.join{left:668px;top:1125px;font-size:11.5px;font-weight:600;color:#444}
.social{position:absolute;top:1120px;width:27px;height:27px;border:1.5px solid #444;border-radius:50%}
</style>
</head>
<body>

<header class="site-header">
  <nav class="abs main-nav"><a href="#">O Nas</a><a href="#">Caste Dotazy</a><a href="#">Kontakt</a></nav>
  <div class="abs brand">POJISTIVO.CZ</div>
  <a class="abs btn-register" href="#">RGISTROVAT</a>
  <a class="abs login" href="#">Prihlasit se</a>
</header>

<section class="abs hero"></section>
<h2 class="abs hero-title" style="left:123px;top:108px">Chcete pojistit neco jineho?</h2>
<h2 class="abs hero-title" style="left:641px;top:110px">Najdete nejvyhodnejsi pojisteni</h2>

<svg class="abs" style="left:141px;top:163px" width="18" height="10" viewBox="0 0 18 10"><polyline points="1,9 9,1 17,9" fill="none" stroke="#222" stroke-width="1.5"/></svg>

<div class="category-list">
  <div class="cat" style="top:184px">
    <span class="cat-icon"><svg width="24" height="14" viewBox="0 0 24 14"><path d="M2 10 L3 6 L7 5 L10 1 L17 1 L20 5 L23 6 L23 10 Z" fill="#222"/><circle cx="7" cy="11" r="2.5" fill="#222"/><circle cx="18" cy="11" r="2.5" fill="#222"/></svg></span>
    <span class="cat-label">Havarijni<br>Pojisteni</span>
  </div>
  <div class="cat" style="top:242px">
    <span class="cat-icon"><svg width="20" height="20" viewBox="0 0 20 20"><path d="M18 3 L12 8 L4 6 L2 8 L9 11 L6 15 L3 15 L2 16 L6 17 L7 19 L8 18 L8 15 L12 12 L15 18 L17 16 L15 8 L20 4 Z" fill="#222"/></svg></span>
    <span class="cat-label">Cestovani<br>Pojisteni</span>
  </div>
  <div class="cat active" style="top:301px">
    <span class="cat-icon"><svg width="22" height="20" viewBox="0 0 22 20"><path d="M3 9 L11 2 L19 9 M5 8 L5 18 L17 18 L17 8" fill="none" stroke="#fff" stroke-width="2"/></svg></span>
    <span class="cat-label">Pojisteni<br>Domova</span>
  </div>
  <div class="cat" style="top:359px">
    <span class="cat-icon"><svg width="22" height="20" viewBox="0 0 22 20"><rect x="8" y="1" width="6" height="3" fill="#222"/><path d="M4 10 L6 5 L16 5 L18 10 L20 10 L20 16 L2 16 L2 10 Z" fill="none" stroke="#222" stroke-width="1.6"/><rect x="3" y="16" width="3" height="3" fill="#222"/><rect x="16" y="16" width="3" height="3" fill="#222"/></svg></span>
    <span class="cat-label">Povinne<br>Ruceni</span>
  </div>
</div>

<svg class="abs" style="left:141px;top:424px" width="18" height="10" viewBox="0 0 18 10"><polyline points="1,1 9,9 17,1" fill="none" stroke="#f07f1e" stroke-width="1.5"/></svg>

<div class="abs house-visual" role="img" aria-label="Ilustrace rodinneho domu"></div>

<form class="quote-form">
  <div class="field" style="top:183px">Jmeno</div>
  <div class="field" style="top:231px">Prijment</div>
  <div class="field" style="top:279px">E-mail</div>
</form>
<div class="abs consent"><span class="box"><i></i></span><span>Souhlasim s <u>podminkami pouziti</u></span></div>
<a class="abs btn-price" href="#">SPOCITAT CENU</a>

<section class="abs why"></section>
<h2 class="abs why-title">Proc hledat pojisteni pres Pojistivo.cz?</h2>

<div class="benefit" style="left:217px;top:587px"><svg width="15" height="15" viewBox="0 0 24 24"><polygon points="12,2 15,9 22,9.5 16.5,14 18.5,21.5 12,17.5 5.5,21.5 7.5,14 2,9.5 9,9" fill="none" stroke="#f07f1e" stroke-width="2"/></svg>S nami najdete tu nejvyhodnejsi nabidku</div>
<div class="benefit" style="left:217px;top:616px"><svg width="15" height="15" viewBox="0 0 24 24"><polygon points="12,2 15,9 22,9.5 16.5,14 18.5,21.5 12,17.5 5.5,21.5 7.5,14 2,9.5 9,9" fill="none" stroke="#f07f1e" stroke-width="2"/></svg>zarucime vam nejlepsi cenu na trhu</div>
<div class="benefit" style="left:217px;top:645px"><svg width="15" height="15" viewBox="0 0 24 24"><polygon points="12,2 15,9 22,9.5 16.5,14 18.5,21.5 12,17.5 5.5,21.5 7.5,14 2,9.5 9,9" fill="none" stroke="#f07f1e" stroke-width="2"/></svg>staci par minut a muzete usetrit tisice</div>
<div class="benefit" style="left:217px;top:674px"><svg width="15" height="15" viewBox="0 0 24 24"><polygon points="12,2 15,9 22,9.5 16.5,14 18.5,21.5 12,17.5 5.5,21.5 7.5,14 2,9.5 9,9" fill="none" stroke="#f07f1e" stroke-width="2"/></svg>srovnavame vsechny pojistovny</div>
<div class="benefit secondary" style="left:537px;top:587px"><svg width="15" height="15" viewBox="0 0 24 24"><polygon points="12,2 15,9 22,9.5 16.5,14 18.5,21.5 12,17.5 5.5,21.5 7.5,14 2,9.5 9,9" fill="none" stroke="#f07f1e" stroke-width="2"/></svg>zridime vam vsechny druhy pojisteni</div>
<div class="benefit secondary" style="left:537px;top:616px"><svg width="15" height="15" viewBox="0 0 24 24"><polygon points="12,2 15,9 22,9.5 16.5,14 18.5,21.5 12,17.5 5.5,21.5 7.5,14 2,9.5 9,9" fill="none" stroke="#f07f1e" stroke-width="2"/></svg>vse vyridite z pohodli domova</div>
<div class="benefit secondary" style="left:537px;top:645px"><svg width="15" height="15" viewBox="0 0 24 24"><polygon points="12,2 15,9 22,9.5 16.5,14 18.5,21.5 12,17.5 5.5,21.5 7.5,14 2,9.5 9,9" fill="none" stroke="#f07f1e" stroke-width="2"/></svg>nemusite nikam chodit a usetrite</div>

<section class="abs info"></section>
<div class="abs review-visual" role="img" aria-label="Fotografie ciferniku hodin s napisem o kontrole pojistky"></div>
<article class="abs info-col" style="left:391px;top:775px">
  <h3>Uxavreli jste v minulosti nevyhodnou pojistku? Zbavte se ji!</h3>
  <p>Lorem Ipsum is simply dummy text of the printing and typesetting industry. Lorem Ipsum has been the industry's standard dummy text ever since the 1500s, when an unknown printer took a galley of type and scrambled it to make a type specimen book. It has survived not only five centuries, but also the leap into electronic typesetting, remaining essentially unchanged. It was popularised in the 1960s with the release including versions of Lorem Ipsum.</p>
</article>
<article class="abs info-col" style="left:669px;top:775px;width:224px">
  <h3>Jak to fungule</h3>
  <p>Lorem Ipsum is simply dummy text of the printing and typesetting industry. Lorem Ipsum has been the industry's standard dummy text ever since the 1500s, when an unknown printer took a galley of type and scrambled it to make a type specimen book. It has survived not only five centuries, but also the leap into electronic typesetting, remaining essentially unchanged.</p>
</article>

<section class="abs newsletter"></section>
<div class="abs band-brand">POJISTIVO.CZ</div>
<div class="abs band-label">ODEBIRAT NEWSLETTER</div>
<div class="abs band-input">E-mail</div>
<a class="abs band-btn" href="#">POTVRDIT</a>

<footer>
  <div class="abs legal">Ochrana Soukromi &nbsp;|&nbsp; Podminky Pouziti</div>
  <div class="abs copyright">© Copyright 2017 Pojistivo.cz. Vsechna prava vyhrazena.</div>
  <div class="abs join">Join us on</div>
  <a class="social" style="left:742px" href="#" aria-label="Socialni sit 1"></a>
  <a class="social" style="left:783px" href="#" aria-label="Socialni sit 2"></a>
  <a class="social" style="left:824px" href="#" aria-label="Socialni sit 3"></a>
  <a class="social" style="left:865px" href="#" aria-label="Socialni sit 4"></a>
</footer>

</body>
</html>
```